GDFH Business Card

Looking for a business card design to incorporate our branding. We want to only use the colors listing in the Branding Package (attached).
Updates

Target Market(s)

People who need their phone or device fixed.

Industry/Entity Type

Electronics

Contact Information for Business Card

Please use:

Gadget Fix Haven LLC
4870 S Ridgecrest Pkwy
Suite 318
San Antonio, TX 78291

Wendell Thorsby, Store Manager

(210) 555-0147

Requirements
Must have
• Must include the colors that are contained within the Branding Package PDF file.

```html
<!DOCTYPE html>
<html lang="en">
<head>
<meta charset="utf-8">
<title>Gadget Fix Haven — Business Card</title>
<link rel="stylesheet" href="https://fonts.googleapis.com/css2?family=Montserrat:wght@400;500;700&display=swap">
<style>
  :root {
    --bg: #ffffff;
    --card: #242424;
    --orange: #f05323;
    --lime: #cfd94a;
    --white: #ffffff;
    --muted: #8a8a8a;
  }
  * { margin: 0; padding: 0; box-sizing: border-box; }
  html, body { width: 1200px; height: 750px; overflow: hidden; background: var(--bg); }
  body { position: relative; font-family: "Montserrat", sans-serif; }

  .card {
    position: absolute;
    width: 520px; height: 300px;
    background: var(--card);
    border-radius: 22px;
    overflow: hidden;
    box-shadow: 0 10px 24px rgba(0,0,0,0.25);
  }
  .card--front { left: 50px; top: 60px; }
  .card--back  { left: 630px; top: 390px; }

  .block { position: absolute; }
  .block--orange { background: var(--orange); }
  .block--lime { background: var(--lime); }

  /* brand mark */
  .brand { position: absolute; display: flex; align-items: center; gap: 14px; white-space: nowrap; }
  .brand__square {
    width: 58px; height: 58px; border-radius: 10px;
    background: var(--orange); flex: none;
  }
  .brand__frame {
    border: 2px solid var(--orange); border-radius: 18px;
    padding: 10px 22px;
  }
  .brand__name {
    color: var(--orange); font-weight: 400; font-size: 30px;
    letter-spacing: 0.5px; white-space: nowrap;
  }
  .card--front .brand { left: 62px; top: 118px; }

  .card--back .brand {
    left: 118px; top: 150px;
    gap: 10px;
    transform: translate(-50%, -50%) rotate(-90deg);
    transform-origin: center;
  }
  .card--back .brand__square { width: 40px; height: 40px; border-radius: 8px; }
  .card--back .brand__frame { padding: 7px 14px; border-radius: 14px; }
  .card--back .brand__name { font-size: 18px; }

  /* contact details */
  .contact { position: absolute; display: flex; align-items: center; gap: 12px; color: var(--white); }
  .icon {
    width: 26px; height: 26px; border-radius: 4px; flex: none;
    display: flex; align-items: center; justify-content: center;
  }
  .icon--orange { background: var(--orange); }
  .icon--lime { background: var(--lime); }
  .contact__phone { left: 232px; top: 70px; font-size: 14px; font-weight: 500; }
  .contact__person { left: 232px; top: 134px; }
  .contact__address { left: 232px; top: 192px; align-items: flex-start; }
  .person__name { font-size: 15px; font-weight: 700; letter-spacing: 0.5px; text-transform: uppercase; color: var(--white); }
  .person__title { font-size: 10px; font-weight: 500; letter-spacing: 1px; text-transform: uppercase; color: var(--card); }
  .address { font-size: 13px; line-height: 1.4; font-weight: 500; }
</style>
</head>
<body>

  <section class="card card--front" aria-label="Card front">
    <div class="block block--orange" style="left:400px; top:52px; width:120px; height:70px;"></div>
    <div class="block block--lime" style="left:508px; top:44px; width:12px; height:8px;"></div>
    <div class="block block--lime" style="left:508px; top:122px; width:12px; height:8px;"></div>
    <div class="block block--orange" style="left:0; top:215px; width:18px; height:62px;"></div>

    <div class="brand">
      <div class="brand__square"></div>
      <div class="brand__frame"><span class="brand__name">Gadget Fix Haven</span></div>
    </div>
  </section>

  <section class="card card--back" aria-label="Card back">
    <div class="block block--orange" style="left:0; top:0; width:16px; height:300px;"></div>
    <div class="block block--lime" style="left:0; top:125px; width:16px; height:60px;"></div>
    <div class="block block--orange" style="left:205px; top:122px; width:315px; height:56px;"></div>
    <div class="block block--lime" style="left:508px; top:114px; width:12px; height:8px;"></div>
    <div class="block block--lime" style="left:508px; top:178px; width:12px; height:8px;"></div>

    <div class="brand">
      <div class="brand__square"></div>
      <div class="brand__frame"><span class="brand__name">Gadget Fix Haven</span></div>
    </div>

    <div class="contact contact__phone">
      <span class="icon icon--orange">
        <svg width="14" height="14" viewBox="0 0 24 24"><path fill="#fff" d="M6.6 10.8a15 15 0 0 0 6.6 6.6l2.2-2.2a1 1 0 0 1 1-.25 11.4 11.4 0 0 0 3.6.57 1 1 0 0 1 1 1V20a1 1 0 0 1-1 1A17 17 0 0 1 3 4a1 1 0 0 1 1-1h3.5a1 1 0 0 1 1 1c0 1.25.2 2.45.57 3.57a1 1 0 0 1-.25 1z"/></svg>
      </span>
      <span>(210) 555-0147</span>
    </div>

    <div class="contact contact__person">
      <span class="icon icon--lime">
        <svg width="14" height="14" viewBox="0 0 24 24"><circle cx="12" cy="8" r="4" fill="#fff"/><path fill="#fff" d="M4 21a8 8 0 0 1 16 0z"/></svg>
      </span>
      <div>
        <div class="person__name">Wendell Thorsby</div>
        <div class="person__title">Store Manager</div>
      </div>
    </div>

    <div class="contact contact__address">
      <span class="icon icon--orange">
        <svg width="14" height="14" viewBox="0 0 24 24"><path fill="#fff" d="M12 2a7 7 0 0 0-7 7c0 5 7 13 7 13s7-8 7-13a7 7 0 0 0-7-7zm0 9.5A2.5 2.5 0 1 1 12 6.5a2.5 2.5 0 0 1 0 5z"/></svg>
      </span>
      <div class="address">
        4870 S Ridgecrest Pkwy<br>
        Suite 318<br>
        San Antonio, TX 78291
      </div>
    </div>
  </section>

</body>
</html>
```